Brivane Redesign

We need a face lift for our website, www.brivane.com. We sell flooring and related products nationwide. We are interested in expanding the width of the website and introducing grays and black. We want the design to be both contemporary and user friendly.

```html
<!DOCTYPE html>
<html lang="en">
<head>
<meta charset="utf-8">
<title>Brivane – Flooring Online</title>
<link href="https://fonts.googleapis.com/css2?family=Open+Sans:wght@400;600;700;800&family=Dancing+Script:wght@600&display=swap" rel="stylesheet">
<style>
:root{
  --red:#e60000;
  --black:#1c1c1c;
  --ink:#333;
  --muted:#666;
  --line:#e2e2e2;
  --page:#f3f3f3;
  --white:#fff;
  --link:#1a6fc4;
}
*{box-sizing:border-box;margin:0;padding:0}
html,body{width:1154px;height:1200px;overflow:hidden}
body{font-family:"Open Sans",Arial,sans-serif;color:var(--ink);background:var(--page);font-size:12px;position:relative}
.wrap{width:942px;margin-left:106px;position:relative}

/* utility bar */
.utility{height:26px;background:var(--black);color:#ddd;font-size:11px}
.utility .wrap{display:flex;justify-content:flex-end;align-items:center;height:26px;gap:14px}
.chat{background:var(--white);color:var(--ink);border-radius:3px;padding:2px 10px 2px 8px;display:flex;align-items:center;gap:8px;height:20px}
.chat b{color:var(--link);font-weight:600}

/* header */
.header{height:98px;background:var(--white)}
.header .wrap{height:98px}
.brand{position:absolute;left:0;top:18px;display:flex;align-items:center;gap:8px}
.brand-mark{width:30px;height:30px;background:var(--red)}
.brand-name{font-size:30px;font-weight:700;color:var(--black);line-height:1}
.brand-tag{position:absolute;left:40px;top:58px;font-size:9px;font-style:italic;font-weight:700;color:var(--black);white-space:nowrap}
.phone{position:absolute;left:672px;top:22px;font-size:17px;font-weight:700;color:var(--black)}
.cart{position:absolute;right:0;top:24px;font-size:12px;display:flex;gap:6px;align-items:center}
.cart em{color:var(--red);font-style:normal}
.search{position:absolute;right:0;top:57px;display:flex;height:29px}
.search span{width:206px;border:1px solid var(--line);padding:6px 12px;font-size:10px;color:#888}
.search b{background:var(--black);color:var(--white);font-weight:400;font-size:13px;padding:5px 10px}

/* nav */
.nav{height:37px;background:var(--red)}
.nav ul{list-style:none;display:flex;gap:18px;height:37px;align-items:center}
.nav li{color:var(--white);font-size:13px}

/* layout */
.body{position:absolute;top:175px;left:106px;width:942px}
.sidebar{position:absolute;left:0;top:0;width:222px}
.box{background:var(--white);box-shadow:0 1px 3px rgba(0,0,0,.2);margin-bottom:13px}
.box h3{background:var(--black);color:var(--white);height:32px;line-height:32px;padding-left:15px;font-size:14px;font-weight:700}
.box ul{list-style:none;padding:4px 14px 8px 15px}
.box li{height:26px;line-height:26px;border-bottom:1px solid var(--line);font-size:12px;display:flex;justify-content:space-between;align-items:center}
.box li:last-child{border-bottom:0}
.plus{width:10px;height:10px;border:1px solid #bbb;position:relative}
.plus::before,.plus::after{content:"";position:absolute;background:#aaa}
.plus::before{left:2px;right:2px;top:4px;height:1px}
.plus::after{top:2px;bottom:2px;left:4px;width:1px}
.promo{padding:10px 12px 12px 14px;height:141px}
.promo p{font-size:11px;font-weight:600;margin-bottom:6px}
.tags{display:flex;flex-wrap:wrap;gap:5px 4px;margin-bottom:8px}
.tags span{border:1px solid var(--line);border-radius:3px;color:var(--link);font-size:11px;line-height:18px;text-align:center;white-space:nowrap}
.promo small{display:block;font-size:10px;color:var(--muted);margin-bottom:8px}
.btn{display:inline-block;background:var(--red);color:var(--white);font-weight:700;font-size:11px;padding:4px 18px;border-radius:3px}

.main{position:absolute;left:236px;top:0;width:706px}
.hero{height:351px;position:relative;background:linear-gradient(180deg,#b9a48a 0%,#8d6b48 45%,#6a4523 100%)}
.sale{position:absolute;left:0;top:127px;width:321px;height:115px;background:var(--black);color:var(--white);padding:8px 0 0 22px}
.sale .ny{font-size:27px;font-weight:700;line-height:1.1}
.sale .big{font-size:58px;font-weight:800;line-height:.95;display:inline-block}
.sale .ship{position:absolute;left:180px;top:59px;font-family:"Dancing Script",cursive;font-size:20px}
.sale .day{position:absolute;left:175px;top:86px;font-size:18px;font-weight:700}
.truck{position:absolute;left:235px;top:90px}
.arrows{position:absolute;right:15px;bottom:16px;display:flex;gap:6px}

.samples{height:148px;position:relative;background:linear-gradient(90deg,#f5ecd8,#fafaf7 60%,#f1efe9);box-shadow:0 1px 3px rgba(0,0,0,.15)}
.samples h2{position:absolute;left:25px;top:22px;font-size:44px;font-weight:700;color:var(--black);line-height:1;letter-spacing:.5px}
.samples h2 span{color:var(--red)}
.samples p{position:absolute;left:24px;font-size:17px;color:#444;line-height:22px;white-space:nowrap}
.samples .btn{position:absolute;left:215px;top:101px;font-size:12px;padding:5px 19px}
.wood{position:absolute;left:430px;top:28px;width:256px;height:110px;background:linear-gradient(135deg,#a8542f,#d8a27a 45%,#e9c9a4);border-radius:4px}

.products{display:flex;gap:20px;margin-top:17px}
.card{width:222px;height:311px;position:relative;box-shadow:0 1px 3px rgba(0,0,0,.2);overflow:hidden}
.card .photo{position:absolute;inset:0}
.card .label{position:absolute;left:0;right:0;bottom:0;height:79px;background:rgba(255,255,255,.85);padding:4px 10px;font-size:15px;line-height:22px;color:var(--black)}
.card .label b{display:block;font-weight:700;font-size:16px}
.burst{position:absolute;left:116px;top:178px;width:100px;height:100px}
.burst div{position:absolute;inset:0;display:flex;flex-direction:column;align-items:center;justify-content:center;color:var(--white);line-height:1}
.burst small{font-size:12px}
.burst strong{font-size:31px;font-weight:700;margin:2px 0}
.burst i{font-style:normal;font-size:12px}
.copy{margin-top:20px;font-size:11.5px;font-weight:700;line-height:21px;color:var(--ink)}

/* footer */
.footer{position:absolute;left:0;top:1080px;width:1154px;height:120px;background:var(--white);border-top:1px solid var(--line)}
.links{position:absolute;left:107px;top:14px;width:560px;font-size:12px;line-height:22px;color:var(--ink)}
.links span{margin:0 5px;color:#999}
.cards{position:absolute;left:107px;top:70px;display:flex;gap:8px}
.cards i{width:38px;height:26px;border-radius:3px;background:#d9d9d9;display:block}
.badges{position:absolute;right:106px;top:16px;width:220px;height:100px}
.badges i{position:absolute;display:block;background:#dcdcdc;border-radius:4px}
</style>
</head>
<body>

<div class="utility">
  <div class="wrap">
    <span class="chat"><svg width="14" height="12" viewBox="0 0 14 12"><path d="M2 1h10a1 1 0 0 1 1 1v6a1 1 0 0 1-1 1H6l-3 2V9H2a1 1 0 0 1-1-1V2a1 1 0 0 1 1-1z" fill="none" stroke="#e60000" stroke-width="1.4"/></svg>Live Chat <b>OFFLINE</b></span>
    <span>&#9906; Order tracking</span>
    <span>? FAQ</span>
    <span>&#9786; My Account</span>
  </div>
</div>

<header class="header">
  <div class="wrap">
    <div class="brand"><span class="brand-mark"></span><span class="brand-name">Brivane</span></div>
    <div class="brand-tag">Values Online Since '99</div>
    <div class="phone">1-888-555-0147</div>
    <div class="cart"><svg width="17" height="14" viewBox="0 0 17 14"><path d="M1 1h3l2 8h8l2-6H5" fill="none" stroke="#555" stroke-width="1.4"/><circle cx="7" cy="12" r="1.3" fill="#555"/><circle cx="13" cy="12" r="1.3" fill="#555"/></svg><span><em>0</em> Product(s) in cart</span></div>
    <div class="search"><span>Description or item</span><b>SEARCH</b></div>
  </div>
</header>

<nav class="nav">
  <div class="wrap">
    <ul><li>ALAMINATE</li><li>HARDWOOD</li><li>AREA RUGS</li><li>BAMBOO</li><li>CORK</li><li>VINYL</li><li>CARPET TILE</li><li>TILE</li><li>CLOCKS</li><li>BATH</li><li>CLEARANC</li></ul>
  </div>
</nav>

<div class="body">
  <aside class="sidebar">
    <section class="box">
      <h3>CURRENT PROMOTIONS</h3>
      <div class="promo">
        <p>Offering discount prices on</p>
        <div class="tags">
          <span style="width:70px">laminate</span><span style="width:50px">cork</span><span style="width:68px">vinyl</span>
          <span style="width:70px">hardwood</span><span style="width:56px">bamboo</span><span style="width:62px">area rugs</span>
        </div>
        <small>from the brands you know and trust.</small>
        <span class="btn">Click Here</span>
      </div>
    </section>
    <section class="box">
      <h3>SHOP BY BRAND</h3>
      <ul><li>Laminate<i class="plus"></i></li><li>Hardwood<i class="plus"></i></li><li>Bamboo<i class="plus"></i></li><li>Cork<i class="plus"></i></li><li>vinyl<i class="plus"></i></li><li>Carpet Tile<i class="plus"></i></li><li>Tile<i class="plus"></i></li></ul>
    </section>
    <section class="box">
      <h3>HOME DECOR</h3>
      <ul><li>Area Rugs<i class="plus"></i></li><li>Bath<i class="plus"></i></li><li>Clocks<i class="plus"></i></li></ul>
    </section>
    <section class="box">
      <h3>ACCESSORIES</h3>
      <ul><li>Underlayment<i class="plus"></i></li><li>Trim &amp; Modeling<i class="plus"></i></li><li>Floor Cleaner<i class="plus"></i></li><li>Installation Tools<i class="plus"></i></li></ul>
    </section>
    <section class="box">
      <h3>FLOORING FACTS</h3>
      <ul><li>Laminate<i class="plus"></i></li><li>Hardwood<i class="plus"></i></li><li>Cork<i class="plus"></i></li><li>Area Rugs<i class="plus"></i></li></ul>
    </section>
  </aside>

  <main class="main">
    <section class="hero" role="img" aria-label="Living room with armchair, side table and glossy hardwood floor">
      <div class="sale">
        <div class="ny">NEW YEAR</div>
        <div class="big">SALE</div>
        <div class="ship">free Shipping</div>
        <div class="day">ONE DAY ONLY</div>
      </div>
      <svg class="truck" width="100" height="100" viewBox="-50 -50 100 100">
        <g fill="#fff"><rect x="-38" y="-38" width="76" height="76"/><rect x="-38" y="-38" width="76" height="76" transform="rotate(30)"/><rect x="-38" y="-38" width="76" height="76" transform="rotate(60)"/></g>
        <rect x="-20" y="-16" width="26" height="22" fill="#e60000"/>
        <path d="M7-8h9l6 8v6H7z" fill="#e60000"/>
        <circle cx="-12" cy="9" r="5" fill="#e60000" stroke="#fff" stroke-width="2"/>
        <circle cx="14" cy="9" r="5" fill="#e60000" stroke="#fff" stroke-width="2"/>
      </svg>
      <div class="arrows">
        <svg width="32" height="32" viewBox="0 0 32 32"><circle cx="16" cy="16" r="14" fill="none" stroke="#fff" stroke-width="2.5"/><path d="M19 9l-7 7 7 7" fill="none" stroke="#fff" stroke-width="2.5"/></svg>
        <svg width="32" height="32" viewBox="0 0 32 32"><circle cx="16" cy="16" r="14" fill="none" stroke="#fff" stroke-width="2.5"/><path d="M13 9l7 7-7 7" fill="none" stroke="#fff" stroke-width="2.5"/></svg>
      </div>
    </section>

    <section class="samples">
      <h2><span>FREE</span> SAMPLES</h2>
      <p style="top:79px">Completely Free.</p>
      <p style="top:107px">No credit card required</p>
      <span class="btn">Click Here</span>
      <div class="wood" role="img" aria-label="Stacked hardwood flooring sample pieces"></div>
    </section>

    <section class="products">
      <article class="card">
        <div class="photo" role="img" aria-label="Bright room with white cabinet and striped wall" style="background:linear-gradient(90deg,#eeeae4 0%,#f3efe9 45%,#b06a4b 60%,#d8c3b2 100%)"></div>
        <div class="label"><b>Halvorn</b>Shoreline<br>12mm Laminate</div>
        <svg class="burst" viewBox="-50 -50 100 100"><g fill="#e60000"><rect x="-38" y="-38" width="76" height="76"/><rect x="-38" y="-38" width="76" height="76" transform="rotate(22.5)"/><rect x="-38" y="-38" width="76" height="76" transform="rotate(45)"/><rect x="-38" y="-38" width="76" height="76" transform="rotate(67.5)"/></g></svg>
        <div class="burst"><div><small>Starting at</small><strong>2.49</strong><i>sq.ft</i></div></div>
      </article>
      <article class="card">
        <div class="photo" role="img" aria-label="Kitchen with wood-look wall and steel range hood" style="background:linear-gradient(90deg,#caa483 0%,#e3c2a2 55%,#c79b77 100%)"></div>
        <div class="label"><b>Verdell</b>Terracore<br>Luxury Vinyl Tile</div>
        <svg class="burst" viewBox="-50 -50 100 100"><g fill="#e60000"><rect x="-38" y="-38" width="76" height="76"/><rect x="-38" y="-38" width="76" height="76" transform="rotate(22.5)"/><rect x="-38" y="-38" width="76" height="76" transform="rotate(45)"/><rect x="-38" y="-38" width="76" height="76" transform="rotate(67.5)"/></g></svg>
        <div class="burst"><div><small>Starting at</small><strong>3.79</strong><i>sq.ft</i></div></div>
      </article>
      <article class="card">
        <div class="photo" role="img" aria-label="Warm kitchen with dark wood cabinets and chandelier" style="background:linear-gradient(180deg,#7a3d22 0%,#d9a45c 45%,#6b3219 100%)"></div>
        <div class="label"><b>Halvorn</b>Timber Accents<br>Acacia Hardwood</div>
        <svg class="burst" viewBox="-50 -50 100 100"><g fill="#e60000"><rect x="-38" y="-38" width="76" height="76"/><rect x="-38" y="-38" width="76" height="76" transform="rotate(22.5)"/><rect x="-38" y="-38" width="76" height="76" transform="rotate(45)"/><rect x="-38" y="-38" width="76" height="76" transform="rotate(67.5)"/></g></svg>
        <div class="burst"><div><small>Starting at</small><strong>4.99</strong><i>sq.ft</i></div></div>
      </article>
    </section>

    <p class="copy">©1999-2014 Northfield Value Goods, Inc. All rights reserved. BRIVANE, BRIVANE OUTLET, and BRIVANE.COM are trademarks of Northfield Value Goods, Inc. or its affiliates.</p>
  </main>
</div>

<footer class="footer">
  <div class="links">About us<span>|</span>careers<span>|</span>consumer reviews<span>|</span>contact us<span>|</span>faq<span>|</span>ordering<span>|</span>pricing<span>|</span>privacy policy<br>return policy<span>|</span>shipping<span>|</span>sitemap</div>
  <div class="cards"><i></i><i></i><i></i><i></i><i></i><i></i></div>
  <div class="badges">
    <i style="left:46px;top:0;width:64px;height:38px"></i>
    <i style="left:128px;top:2px;width:92px;height:32px"></i>
    <i style="left:22px;top:62px;width:60px;height:24px"></i>
    <i style="left:94px;top:60px;width:62px;height:32px"></i>
    <i style="left:160px;top:56px;width:60px;height:36px"></i>
  </div>
</footer>

</body>
</html>
```